New Zealand Luggage Importer Needs Business Cards

We need professional, creative and fashionable business cards created.
We are based in New Zealand and import and distribute high-end, quality, fashionable and durable luggage.
We pride ourselves on selling the very best quality luggage, second only to 1 brand (which we won't mention here)...we use the same manufacturer. However, our prices are much more reasonable.
Industry/Entity Type
Business
Contact Information for Business Card
Mark Dunsley
027 512 4068
3/17 Harlow Street, Pinecrest Flats, Auckland, 0614
PO Box 204377, Fernside, Auckland 0731
09-528-3916
sales@brivancases.co.nz / www.brivancases.co.nz

```html
<!DOCTYPE html>
<html lang="en">
<head>
<meta charset="utf-8">
<title>Brivan Cases – Business Cards</title>
<link rel="stylesheet" href="https://fonts.googleapis.com/css2?family=Open+Sans:wght@400;600;700&display=swap">
<style>
  :root {
    --stage: #e9e6e1;
    --card-black: #1f1d1e;
    --card-black-deep: #161415;
    --gold: #c9b454;
    --gold-dark: #9c8a32;
    --gold-light: #ddd07e;
    --white: #ffffff;
    --text-soft: #f1f1f1;
  }
  * { margin: 0; padding: 0; box-sizing: border-box; }
  html, body { width: 1200px; height: 780px; overflow: hidden; }
  body {
    background: var(--stage);
    font-family: "Open Sans", Arial, sans-serif;
    display: flex;
    align-items: center;
    justify-content: center;
    gap: 40px;
  }
  .card {
    position: relative;
    width: 540px;
    height: 300px;
    border-radius: 4px;
    overflow: hidden;
    background: linear-gradient(160deg, var(--card-black) 0%, var(--card-black-deep) 100%);
    box-shadow: 0 10px 24px rgba(0,0,0,0.22);
  }
  .card-front__shapes { position: absolute; inset: 0; width: 100%; height: 100%; }
  .card-front__content {
    position: absolute;
    left: 34px;
    top: 30px;
    color: var(--text-soft);
  }
  .brand-name {
    font-family: "Open Sans", Arial, sans-serif;
    font-weight: 700;
    color: var(--white);
    letter-spacing: 0.04em;
    text-transform: uppercase;
    white-space: nowrap;
  }
  .card-front .brand-name { font-size: 40px; line-height: 1; }
  .holder-name {
    margin: 22px 0 0 44px;
    font-size: 22px;
    font-weight: 700;
    color: var(--white);
  }
  .contact-block {
    margin: 12px 0 0 68px;
    font-size: 14.5px;
    line-height: 1.38;
    font-style: normal;
  }
  .contact-list { list-style: none; margin-top: 8px; }
  .contact-label { color: var(--gold); font-weight: 600; margin-right: 4px; }
  .card-back {
    display: flex;
    flex-direction: column;
    align-items: center;
    justify-content: center;
    gap: 16px;
  }
  .card-back .brand-name { font-size: 46px; }
  .web-address { color: var(--gold); font-size: 15px; letter-spacing: 0.02em; }
</style>
</head>
<body>
  <section class="card card-front" aria-label="Business card front">
    <svg class="card-front__shapes" viewBox="0 0 540 300" aria-hidden="true">
      <defs>
        <linearGradient id="goldSweep" x1="0" y1="0" x2="1" y2="1">
          <stop offset="0" stop-color="#ddd07e"/>
          <stop offset="0.5" stop-color="#c9b454"/>
          <stop offset="1" stop-color="#9c8a32"/>
        </linearGradient>
        <linearGradient id="blackFace" x1="0" y1="0" x2="1" y2="1">
          <stop offset="0" stop-color="#1f1d1e"/>
          <stop offset="1" stop-color="#161415"/>
        </linearGradient>
      </defs>
      <rect width="540" height="300" fill="url(#goldSweep)"/>
      <circle cx="135" cy="200" r="375" fill="#ffffff"/>
      <circle cx="120" cy="205" r="360" fill="url(#blackFace)"/>
    </svg>
    <div class="card-front__content">
      <p class="brand-name">Brivan Cases</p>
      <p class="holder-name">Mark Dunsley</p>
      <address class="contact-block">
        PO Box 204377<br>
        Fernside, Auckland 0731<br>
        3/17 Harlow Street<br>
        Pinecrest Flats, Auckland, 0614
        <ul class="contact-list">
          <li><span class="contact-label">M:</span>027 512 4068</li>
          <li><span class="contact-label">P:</span>09-528-3916</li>
          <li><span class="contact-label">E:</span>sales@brivancases.co.nz</li>
        </ul>
      </address>
    </div>
  </section>

  <section class="card card-back" aria-label="Business card back">
    <p class="brand-name">Brivan Cases</p>
    <p class="web-address">www.brivancases.co.nz</p>
  </section>
</body>
</html>
```